Updated Power Point template design

We need an updated Power Point design template. Please see attach business card for branding, would like to incorporate the blue and black corner design aspect some how.

Attached a sample of current PP

Target Market(s)

Corporate Clients

Industry/Entity Type

Electronics

Requirements
Must have
• We require a whole slide deck ( Title side etc )
Nice to have
• Nice amount of white space on slide

```html
<!DOCTYPE html>
<html lang="en">
<head>
<meta charset="utf-8">
<title>Business Partnership Review</title>
<link href="https://fonts.googleapis.com/css2?family=Exo+2:wght@600;700&display=swap" rel="stylesheet">
<style>
  :root {
    --black: #000000;
    --white: #ffffff;
    --brand-blue: #1570bd;
    --text-dark: #1b1b1b;
  }
  html, body {
    margin: 0;
    padding: 0;
    overflow: hidden;
    background: var(--black);
  }
  .slide {
    position: relative;
    width: 1200px;
    height: 900px;
    overflow: hidden;
    background: var(--black);
    font-family: "Exo 2", "Segoe UI", sans-serif;
  }
  .slide__backdrop {
    position: absolute;
    inset: 0;
    width: 1200px;
    height: 900px;
  }
  .slide__content {
    position: absolute;
    left: 544px;
    top: 186px;
  }
  .slide__title {
    margin: 0;
    font-size: 35px;
    font-weight: 700;
    color: var(--brand-blue);
    letter-spacing: 0.2px;
  }
  .slide__date {
    margin: 18px 0 0;
    font-size: 26px;
    font-weight: 700;
    color: var(--text-dark);
  }
  .slide__address {
    margin: 16px 0 0;
    font-size: 19.5px;
    font-weight: 700;
    color: var(--text-dark);
  }
  .attendees {
    list-style: none;
    margin: 18px 0 0;
    padding: 0;
    font-size: 17.5px;
    font-weight: 700;
    color: var(--brand-blue);
    line-height: 29.5px;
  }
  .partner {
    position: absolute;
    top: 632px;
    display: flex;
    align-items: center;
    gap: 9px;
    font-size: 21px;
    font-weight: 700;
    color: var(--brand-blue);
    white-space: nowrap;
    line-height: 26px;
  }
  .partner--meridian { left: 630px; }
  .partner--clearwave { left: 880px; }
  .partner--norvale { left: 1050px; }
  .partner__dot {
    width: 20px;
    height: 20px;
    border-radius: 50%;
    background: var(--brand-blue);
    flex: none;
  }
</style>
</head>
<body>
  <main class="slide">
    <svg class="slide__backdrop" viewBox="0 0 1200 900" aria-hidden="true">
      <path class="backdrop__white-field" fill="var(--white)"
            d="M690,0 C480,80 300,260 310,470 C320,680 700,840 1200,848 L1200,0 Z"/>
      <path class="backdrop__blue-arc" fill="var(--brand-blue)"
            d="M650,22 C470,105 330,272 338,472 C348,665 705,812 1200,826 L1200,834 C720,828 372,672 362,476 C352,282 492,112 664,28 Z"/>
    </svg>

    <section class="slide__content">
      <h1 class="slide__title">Business Partnership Review</h1>
      <p class="slide__date">January 21, 2016</p>
      <p class="slide__address">Clearwave Acoustics Inc. , 218 Research Park Dr., Fairview, PA</p>
      <ul class="attendees">
        <li>Prepared for : Clearwave Acoustics Management Team</li>
        <li>Daniel Hartley -- Materials Manager</li>
        <li>Mark Ellison – Comptroller</li>
        <li>Paul Brenner -- Facility Manager</li>
        <li>Greg Amato &nbsp;-- Purchasing</li>
        <li>Lisa Marie Donovan – Purchasing</li>
        <li>To be determined -- Production Managers</li>
      </ul>
    </section>

    <div class="partner partner--meridian"><span class="partner__dot"></span>Meridian Imaging</div>
    <div class="partner partner--clearwave">clearwave<span class="partner__dot"></span></div>
    <div class="partner partner--norvale"><span class="partner__dot"></span>Norvale</div>
  </main>
</body>
</html>
```